Pharmacy in Bahamas needs to Promote Free Kids Multi-Vitamins

We need an advertisement design for a small pharmacy in the Bahamas. This ad is to attract parents to Bright Meadow Pharmacy. Bright Meadow Pharmacy is offering free multi-vitamins to kids whose parents fill their prescriptions at our pharmacy. The campaign will be printed in store on 5.5" x 8.5 sized prints, and posted online. All submissions should be double-sided. Any images of school children should be uniformed.

Parents can sign their kids up to receive free multi-vitamins each time a parent fills a monthly prescription with Bright Meadow Pharmacy.

Fineprint: Parents can receive a maximum of three kid's multi-vitamins per month as supplies last.

Target Market(s)

Parents of Elementary School Children,

Industry/Entity Type

Pharmacy

Font styles to use
Sans Serif

Requirements
Must have
• Crisp, Modern design. Image of Child (in school uniform) and parent.
Nice to have
• Happy Mixed-Raced Children and Parents
Should not have
• Nothing polarizing, too much text. See image of previous ad for "not to do"

```html
<!DOCTYPE html>
<html lang="en">
<head>
<meta charset="utf-8">
<title>Bright Meadow Pharmacy – Free Kids Multi-Vitamins</title>
<link href="https://fonts.googleapis.com/css2?family=Alfa+Slab+One&family=Ubuntu:wght@400;500&display=swap" rel="stylesheet">
<style>
  :root {
    --backdrop: #2e2e2e;
    --paper: #ffffff;
    --brand-red: #c0201f;
    --brand-green: #2e8a35;
    --ink: #1c1c1c;
    --ink-grey: #6b6b6b;
  }
  * { box-sizing: border-box; margin: 0; padding: 0; }
  html, body {
    width: 786px; height: 1200px; overflow: hidden;
    background: var(--backdrop);
  }
  .flyer {
    position: absolute; left: 38px; top: 47px;
    width: 717px; height: 1108px;
    background: var(--paper);
    overflow: hidden;
  }
  .flyer__art { position: absolute; inset: 0; }

  .brand__dot {
    position: absolute; left: 52px; top: 52px;
    width: 76px; height: 76px; border-radius: 50%;
    background: var(--brand-red);
  }
  .brand__name {
    position: absolute; left: 184px; top: 64px;
    font-family: 'Ubuntu', sans-serif; font-weight: 500;
    font-size: 36px; line-height: 1; color: var(--brand-red);
    font-variant: small-caps; letter-spacing: 0.5px; white-space: nowrap;
  }
  .brand__former {
    position: absolute; left: 220px; top: 127px;
    font-family: 'Ubuntu', sans-serif; font-weight: 400;
    font-size: 22px; line-height: 1; color: var(--ink); letter-spacing: 0.6px;
    white-space: nowrap;
  }

  .offer { font-family: 'Alfa Slab One', serif; font-weight: 400; line-height: 1; }
  .offer__line { position: absolute; left: 33px; white-space: nowrap; }
  .offer__free  { top: 486px; font-size: 88px; color: var(--brand-red); letter-spacing: 5px; }
  .offer__item  { top: 576px; font-size: 28px; color: var(--brand-green); letter-spacing: 0.5px; }
  .offer__who   { top: 608px; font-size: 64px; color: var(--brand-green); letter-spacing: 1px; }
  .offer__terms { top: 674px; font-size: 20px; color: var(--ink-grey); line-height: 30px; letter-spacing: 0.6px; }
  .offer__place { top: 734px; font-size: 52px; color: var(--brand-red); letter-spacing: 0.5px; }

  .contact {
    position: absolute; left: 32px; top: 930px;
    font-family: 'Ubuntu', sans-serif; font-size: 20px; color: #fff;
    list-style: none; line-height: 1.3;
  }
  .contact__row { display: flex; align-items: flex-start; gap: 8px; }
  .contact__row + .contact__row { margin-top: 8px; }
  .contact__icon { width: 16px; height: 18px; margin-top: 4px; flex: none; fill: #fff; }

  .fineprint {
    position: absolute; right: 34px; top: 1010px;
    font-family: 'Ubuntu', sans-serif; font-size: 16.5px; color: #fff;
    text-align: right; line-height: 22px;
  }
</style>
</head>
<body>
<main class="flyer">
  <svg class="flyer__art" viewBox="0 0 717 1108" width="717" height="1108">
    <defs>
      <linearGradient id="heroTones" x1="0" y1="0" x2="1" y2="1">
        <stop offset="0" stop-color="#ffffff" stop-opacity="0"/>
        <stop offset="0.28" stop-color="#f6e6d2"/>
        <stop offset="0.48" stop-color="#e9c39c"/>
        <stop offset="0.62" stop-color="#efe6dc"/>
        <stop offset="0.8" stop-color="#a9b8d8"/>
        <stop offset="1" stop-color="#7f94c4"/>
      </linearGradient>
      <linearGradient id="insetTones" x1="0" y1="0" x2="0" y2="1">
        <stop offset="0" stop-color="#b9d98e"/>
        <stop offset="0.3" stop-color="#a46c45"/>
        <stop offset="0.62" stop-color="#7b4a2d"/>
        <stop offset="0.8" stop-color="#6ea43e"/>
        <stop offset="1" stop-color="#4f8a2c"/>
      </linearGradient>
    </defs>

    <path class="hero-photo" role="img" aria-label="Photo of a smiling mother hugging her daughter in a blue school uniform"
          d="M0 222 Q290 185 430 215 Q620 285 717 420 L717 640 Q330 860 0 812 Z" fill="url(#heroTones)"/>

    <path class="swoosh swoosh--line" d="M0 220 Q160 196 300 190" stroke="var(--brand-green)" stroke-width="2.5" fill="none"/>
    <path class="swoosh swoosh--green" d="M290 189 Q560 200 717 300 L717 360 Q580 250 420 205 Q360 195 290 189 Z" fill="var(--brand-green)"/>
    <path class="swoosh swoosh--red" d="M420 205 Q590 250 717 360 L717 420 Q620 285 430 215 Z" fill="var(--brand-red)"/>

    <path class="band band--line" d="M0 812 Q330 860 717 640" stroke="var(--brand-red)" stroke-width="2" fill="none"/>
    <path class="band band--green" d="M0 862 Q330 872 717 690 L717 725 Q320 895 0 910 Z" fill="var(--brand-green)"/>
    <path class="band band--red" d="M0 910 Q320 895 717 725 L717 1108 L0 1108 Z" fill="var(--brand-red)"/>

    <circle class="inset-photo" role="img" aria-label="Photo of two smiling children lying on the grass"
            cx="589" cy="870" r="124" fill="url(#insetTones)" stroke="var(--brand-green)" stroke-width="5"/>
  </svg>

  <header class="brand">
    <span class="brand__dot"></span>
    <h1 class="brand__name">Bright Meadow Pharmacy</h1>
    <p class="brand__former">FORMERLY K.T.S. DRUGS CO. LTD.</p>
  </header>

  <section class="offer">
    <p class="offer__line offer__free">FREE</p>
    <p class="offer__line offer__item">multi-vitamins</p>
    <p class="offer__line offer__who">to kids</p>
    <p class="offer__line offer__terms">whose parents fill their<br>prescriptions at our</p>
    <p class="offer__line offer__place">pharmacy</p>
  </section>

  <ul class="contact">
    <li class="contact__row">
      <svg class="contact__icon" viewBox="0 0 16 18"><path d="M8 0a6 6 0 0 0-6 6c0 4.5 6 12 6 12s6-7.5 6-12a6 6 0 0 0-6-6zm0 8.5A2.5 2.5 0 1 1 8 3.5a2.5 2.5 0 0 1 0 5z"/></svg>
      <span>12 Harbour View Road, K.T.S. Mini Mall<br>P.O.Box F 51873, Freeport,<br>Grand Bahama, Bahamas</span>
    </li>
    <li class="contact__row">
      <svg class="contact__icon" viewBox="0 0 16 18"><path d="M3.5 1.5l2.5 0 1.5 4-2 1.5c1 2.2 2.3 3.6 4.5 4.8l1.6-2 4 1.6v2.6c0 1-1 1.8-2 1.7C7 15.2 1.5 9.6 1.6 3.4c0-1 .9-1.9 1.9-1.9z"/></svg>
      <span>(242) 555 0142</span>
    </li>
    <li class="contact__row">
      <svg class="contact__icon" viewBox="0 0 16 18"><path d="M4 2h8v4H4zM1 7h14v7h-3v3H4v-3H1zM5 12v3h6v-3z"/></svg>
      <span>(242) 555 0148</span>
    </li>
  </ul>

  <p class="fineprint">*Parents can receive a maximum<br>of three kid's multi-vitamins<br>per month as supplies last</p>
</main>
</body>
</html>
```